"Harmony Pouch" - Envelope Package for 3 Small Pamphlets/Tracts

We need a design for an envelope package that will be folded to fit 3 small tracts/pamphlets. The final product will be paper that is simply folded - not glued or stapled. The tracts/pamphlets themselves are the ones that can be found at www.tulomerin.ca/literature - they don't need to be designed as we already have them in print. We just want a package/envelope to put them in so we can hand them out in a creative way.

We are looking for a few different ideas to choose from - which is why we are coming to you! Attached is a design brief that outlines the desired format and pictures of mocked-finished product. Also attached is the "G" (TULO logo). One of the pictures will provide you with the final product measurement in millimetres. You will have to add safety margins for full bleed to send to the printer. This needs to be designed in Photoshop or Illustrator. Photoshop is preferred.

Although I like the white background because it looks clean, please also provide a darker background to see if the "wallet" effect would work. (I am talking about the outside of the package. the inside should remain white.)

I like the concept of the icons for body and mind, but the icon for "spirit" should be something like a generic sunrise, sunset or peaceful lake.

You will notice that there are "folding" numbers inside the attached mockup picture. We would like them to be nicely designed on the final product so that people know how to fold the envelope, but those numbers should be hidden behind the flaps/pamphlets once the 3 pamphlets are in and the product is fully folded. We would also like to have light grey dotted lines to know where to fold on the inside of the package.

On the centre back panel is where you have the question that states "Know someone who needs healing?"

```html
<!DOCTYPE html>
<html lang="en">
<head>
<meta charset="utf-8">
<title>Harmony Pouch – Envelope Dieline</title>
<link rel="stylesheet" href="https://fonts.googleapis.com/css2?family=Arimo:wght@400;700&family=Noticia+Text:ital,wght@1,400;1,700&display=swap">
<style>
  :root {
    --navy: #04335f;
    --paper: #ffffff;
    --bleed: #e8141b;
    --cut: #111111;
    --fold: #a9a9a9;
    --fold-outside: #c9d2de;
    --marker: #8f8f8f;
    --ink: #000000;
  }
  html, body {
    margin: 0;
    padding: 0;
    width: 810px;
    height: 1200px;
    overflow: hidden;
    background: var(--paper);
  }
  .dieline-sheet {
    display: block;
    width: 810px;
    height: 1200px;
  }
  .bleed-line { fill: none; stroke: var(--bleed); stroke-width: 4; }
  .cut-line { stroke: var(--cut); stroke-width: 4; }
  .cut-line.inside { fill: var(--paper); }
  .cut-line.outside { fill: var(--navy); }
  .fold-line { stroke: var(--fold); stroke-width: 2; stroke-dasharray: 9 6; fill: none; }
  .fold-line.on-navy { stroke: var(--fold-outside); }
  .fold-marker { fill: var(--marker); }
  .fold-marker .stem { fill: none; stroke: var(--marker); stroke-width: 10; stroke-linecap: round; }
  .marker-number { font-family: "Arimo", Arial, sans-serif; font-size: 14px; fill: var(--paper); font-weight: 700; text-anchor: middle; }
  .side-title { font-family: "Arimo", Arial, sans-serif; font-size: 78px; fill: var(--ink); text-anchor: middle; }
  .flap-label { font-family: "Noticia Text", Georgia, serif; font-style: italic; font-size: 40px; fill: var(--paper); text-anchor: middle; }
  .headline { font-family: "Noticia Text", Georgia, serif; font-style: italic; font-size: 60px; fill: var(--paper); text-anchor: middle; }
  .product-name { font-family: "Noticia Text", Georgia, serif; font-style: italic; font-weight: 700; font-size: 64px; fill: var(--paper); text-anchor: middle; }
  .brand-name { font-family: "Noticia Text", Georgia, serif; font-style: italic; font-weight: 700; font-size: 50px; fill: var(--navy); }
  .icon-frame { fill: none; stroke: var(--paper); stroke-width: 3; }
  .legend { font-family: "Arimo", Arial, sans-serif; font-weight: 700; font-size: 80px; }
  .legend.cut { fill: var(--ink); }
  .legend.bleed { fill: var(--bleed); }
  .legend.fold { fill: var(--fold); }
</style>
</head>
<body>
<svg class="dieline-sheet" viewBox="0 0 1568 2322" xmlns="http://www.w3.org/2000/svg">
  <defs>
    <symbol id="fold-arrow" viewBox="-32 -32 64 64">
      <g class="fold-marker">
        <path class="stem" d="M-16 18 Q-22 -4 4 -4"/>
        <polygon points="2,-20 28,-4 2,12"/>
      </g>
    </symbol>
    <linearGradient id="tone-runner" x1="0" y1="0" x2="0" y2="1">
      <stop offset="0" stop-color="#3b6f96"/>
      <stop offset="0.55" stop-color="#f2a23a"/>
      <stop offset="0.75" stop-color="#5a3a1e"/>
      <stop offset="1" stop-color="#1c140c"/>
    </linearGradient>
    <radialGradient id="tone-mind" cx="0.5" cy="0.45" r="0.6">
      <stop offset="0" stop-color="#ff5a3c"/>
      <stop offset="0.45" stop-color="#b32a6a"/>
      <stop offset="1" stop-color="#1a2c8c"/>
    </radialGradient>
    <radialGradient id="tone-sunrise" cx="0.5" cy="0.55" r="0.65">
      <stop offset="0" stop-color="#fff3c2"/>
      <stop offset="0.35" stop-color="#f7b342"/>
      <stop offset="1" stop-color="#5d6d8e"/>
    </radialGradient>
  </defs>

  <!-- INSIDE -->
  <g class="inside-spread">
    <path class="bleed-line" d="M228 98 H1340 V636 H1433 V753 H1340 V847 H228 V753 H135 V636 H228 Z"/>
    <path class="cut-line inside" d="M252 122 H1316 V660 H1410 V730 H1316 V823 H252 V730 H158 V660 H252 Z"/>
    <line class="fold-line" x1="252" y1="214" x2="1316" y2="214"/>
    <line class="fold-line" x1="252" y1="730" x2="1316" y2="730"/>
    <line class="fold-line" x1="610" y1="122" x2="610" y2="823"/>
    <line class="fold-line" x1="967" y1="122" x2="967" y2="823"/>

    <use href="#fold-arrow" x="176" y="664" width="60" height="60"/>
    <text class="marker-number" x="198" y="712" style="fill:var(--paper)">1</text>
    <g transform="translate(1364 694) scale(-1 1)"><use href="#fold-arrow" x="-30" y="-30" width="60" height="60"/></g>
    <text class="marker-number" x="1370" y="712">2</text>
    <g transform="translate(785 787) rotate(-90)"><use href="#fold-arrow" x="-30" y="-30" width="60" height="60"/></g>
    <text class="marker-number" x="771" y="801">3</text>
    <g transform="translate(785 156) rotate(90)"><use href="#fold-arrow" x="-30" y="-30" width="60" height="60"/></g>
    <text class="marker-number" x="771" y="156">4</text>
    <g transform="translate(1000 472) scale(-1 1)"><use href="#fold-arrow" x="-30" y="-30" width="60" height="60"/></g>
    <text class="marker-number" x="1008" y="489">5</text>
    <use href="#fold-arrow" x="540" y="442" width="60" height="60"/>
    <text class="marker-number" x="564" y="489">6</text>

    <text class="side-title" x="784" y="940">INSIDE</text>
  </g>

  <!-- OUTSIDE -->
  <g class="outside-spread">
    <path class="bleed-line" d="M228 1003 H1340 V1541 H1433 V1658 H1340 V1752 H228 V1658 H135 V1541 H228 Z"/>
    <path class="cut-line outside" d="M252 1027 H1316 V1565 H1410 V1636 H1316 V1728 H252 V1636 H158 V1565 H252 Z"/>
    <line class="fold-line on-navy" x1="252" y1="1120" x2="1316" y2="1120"/>
    <line class="fold-line on-navy" x1="252" y1="1636" x2="1316" y2="1636"/>
    <line class="fold-line on-navy" x1="600" y1="1027" x2="600" y2="1728"/>
    <line class="fold-line on-navy" x1="958" y1="1027" x2="958" y2="1728"/>

    <g class="flap-labels">
      <text class="flap-label" transform="translate(425 1060) rotate(180)">Spirit</text>
      <text class="flap-label" transform="translate(778 1058) rotate(180)">Mind</text>
      <text class="flap-label" transform="translate(1136 1058) rotate(180)">Body</text>
    </g>

    <text class="headline">
      <tspan x="778" y="1228">Know</tspan>
      <tspan x="778" y="1290">someone</tspan>
      <tspan x="778" y="1352">who</tspan>
      <tspan x="778" y="1414">needs</tspan>
      <tspan x="778" y="1476">healing?</tspan>
    </text>

    <g class="brand-block">
      <rect x="958" y="1167" width="358" height="113" fill="var(--paper)"/>
      <circle cx="1042" cy="1223" r="30" fill="var(--navy)"/>
      <text class="brand-name" x="1090" y="1240">TULO</text>
    </g>

    <text class="product-name">
      <tspan x="1142" y="1392">Harmony</tspan>
      <tspan x="1142" y="1472">Pouch</tspan>
    </text>

    <g class="cover-icons">
      <g role="img" aria-label="Photo of a runner at sunset"><rect x="662" y="1525" width="66" height="66" rx="8" fill="url(#tone-runner)"/><rect class="icon-frame" x="662" y="1525" width="66" height="66" rx="8"/></g>
      <g role="img" aria-label="Illustration of a glowing brain"><rect x="751" y="1525" width="66" height="66" rx="8" fill="url(#tone-mind)"/><rect class="icon-frame" x="751" y="1525" width="66" height="66" rx="8"/></g>
      <g role="img" aria-label="Photo of a sunrise over the horizon"><rect x="841" y="1525" width="66" height="66" rx="8" fill="url(#tone-sunrise)"/><rect class="icon-frame" x="841" y="1525" width="66" height="66" rx="8"/></g>
      <g role="img" aria-label="Photo of a runner at sunset"><rect x="1019" y="1525" width="66" height="66" rx="8" fill="url(#tone-runner)"/><rect class="icon-frame" x="1019" y="1525" width="66" height="66" rx="8"/></g>
      <g role="img" aria-label="Illustration of a glowing brain"><rect x="1108" y="1525" width="66" height="66" rx="8" fill="url(#tone-mind)"/><rect class="icon-frame" x="1108" y="1525" width="66" height="66" rx="8"/></g>
      <g role="img" aria-label="Photo of a sunrise over the horizon"><rect x="1198" y="1525" width="66" height="66" rx="8" fill="url(#tone-sunrise)"/><rect class="icon-frame" x="1198" y="1525" width="66" height="66" rx="8"/></g>
    </g>

    <g class="flap-icons">
      <g role="img" aria-label="Photo of a sunrise, upside down on the flap"><rect x="393" y="1650" width="66" height="66" rx="8" fill="url(#tone-sunrise)" transform="rotate(180 426 1683)"/><rect class="icon-frame" x="393" y="1650" width="66" height="66" rx="8"/></g>
      <g role="img" aria-label="Illustration of a glowing brain, upside down on the flap"><rect x="751" y="1650" width="66" height="66" rx="8" fill="url(#tone-mind)" transform="rotate(180 784 1683)"/><rect class="icon-frame" x="751" y="1650" width="66" height="66" rx="8"/></g>
      <g role="img" aria-label="Photo of a runner at sunset, upside down on the flap"><rect x="1104" y="1650" width="66" height="66" rx="8" fill="url(#tone-runner)" transform="rotate(180 1137 1683)"/><rect class="icon-frame" x="1104" y="1650" width="66" height="66" rx="8"/></g>
    </g>

    <text class="side-title" x="784" y="1845">OUTSIDE</text>
  </g>

  <!-- LEGEND -->
  <g class="legend-block">
    <text class="legend cut" x="385" y="2030">Black Line : Cut Line</text>
    <text class="legend bleed" x="385" y="2118">Rad Line : Bleed Line</text>
    <text class="legend fold" x="385" y="2206">Gray Line : Fold Line</text>
  </g>
</svg>
</body>
</html>
```